Post it Note design

POST-IT NOTE DESIGN (CONTENT)
Size recommended: 4x6 for handwriting space.
Header (Bold):
Lighting Issue Detected on Your Property
Sub-header:
During our routine night inspection, we noted the following item(s):
Checkbox List:
⬜ Building Lights Out
⬜ Pole Lights Out
⬜ Sign Not Illuminated
⬜ Other ________________________
Action Line:
We can provide a quote or dispatch service right away.
Area for notes
Contact Block (Bold & Centered):
Brovane Fixture Inc.
Service@BrovaneFixture.com
www.BrovaneFixture.com
877-514-0862
Industry/Entity Type
Electrical lighting
Colors
Designer to choose colors to be used in the design.
Look and feel
Each slider illustrates characteristics of the customer's brand and the style your logo design should communicate.

```html
<!DOCTYPE html>
<html lang="en">
<head>
<meta charset="utf-8">
<title>Lighting Issue Detected – Brovane Fixture Inc.</title>
<link href="https://fonts.googleapis.com/css2?family=Anton&family=Sora:wght@400;600;700&display=swap" rel="stylesheet">
<style>
  :root {
    --navy: #141f7a;
    --royal: #2f3f9c;
    --red: #e3141f;
    --paper: #f7f7f8;
    --ink: #1b2682;
    --muted: #c4c6cc;
    --backdrop: #b4b4b4;
  }
  * { box-sizing: border-box; margin: 0; padding: 0; }
  html, body { width: 1200px; height: 1200px; overflow: hidden; }
  body { background: var(--backdrop); font-family: "Sora", sans-serif; }

  .note {
    position: absolute; left: 220px; top: 30px;
    width: 760px; height: 1140px;
    background: var(--paper);
    overflow: hidden;
    box-shadow: 0 20px 40px rgba(0,0,0,.18);
  }
  .header-bands { position: absolute; left: 0; top: 0; }
  .headline {
    position: absolute; left: 0; top: 48px; width: 100%;
    text-align: center; color: #fff;
    font-family: "Anton", sans-serif; font-size: 70px; line-height: 1.02;
    letter-spacing: 1px; text-transform: uppercase;
  }
  .subhead {
    position: absolute; left: 110px; top: 268px; width: 540px;
    text-align: center; color: #fff; font-size: 25px; line-height: 1.3; font-weight: 400;
  }

  .checklist { position: absolute; left: 140px; top: 410px; list-style: none; }
  .checklist li {
    display: flex; align-items: center; gap: 26px;
    height: 70px; font-size: 36px; color: var(--ink);
  }
  .checkbox { width: 40px; height: 40px; border: 3px solid var(--ink); flex: none; }
  .write-line { width: 380px; height: 2px; background: var(--ink); margin-left: 12px; margin-top: 18px; }

  .notes-box {
    position: absolute; left: 160px; top: 740px; width: 570px; height: 205px;
    border: 2px dotted var(--ink); border-radius: 18px;
  }
  .notes-label {
    position: absolute; left: 14px; top: 192px;
    transform: rotate(-90deg); transform-origin: left top;
    font-size: 28px; color: var(--muted); letter-spacing: 2px; white-space: nowrap;
  }
  .action-tab {
    position: absolute; left: 140px; top: 718px; width: 560px; height: 100px;
    background: var(--navy); border-radius: 20px 20px 0 0;
    color: #fff; font-weight: 700; font-size: 26px; line-height: 1.3;
    text-align: center; padding-top: 14px;
  }

  .photo { position: absolute; }
  .photo-fixtures {
    left: 0; top: 960px; width: 225px; height: 100px;
    background: linear-gradient(160deg, #dfe3e8, #8d949c 60%, #4a4f55);
  }
  .photo-truck {
    left: 530px; top: 955px; width: 230px; height: 105px;
    background: linear-gradient(180deg, #f2f2f2, #d6d8db 60%, #8a8e93);
  }
  .brand {
    position: absolute; left: 230px; top: 992px; width: 295px;
    display: flex; align-items: center; gap: 8px; justify-content: center;
    font-weight: 700; font-size: 22px; color: var(--navy); line-height: 1.1;
    white-space: nowrap;
  }
  .brand-dot { width: 14px; height: 14px; border-radius: 50%; background: var(--red); flex: none; }

  .contact-bar { position: absolute; left: 0; top: 1060px; width: 760px; height: 80px; display: flex; }
  .phone-block {
    width: 340px; background: var(--red); color: #fff;
    display: flex; align-items: center; justify-content: center; gap: 10px;
    font-weight: 600; font-size: 40px;
  }
  .web-block {
    flex: 1; background: var(--navy); color: #fff;
    display: flex; flex-direction: column; justify-content: center;
    padding-left: 24px; font-size: 19px; line-height: 1.5;
  }
  .web-block span { display: flex; align-items: center; gap: 10px; }
</style>
</head>
<body>
  <article class="note">
    <svg class="header-bands" width="760" height="360" viewBox="0 0 760 360" aria-hidden="true">
      <rect x="0" y="0" width="760" height="250" fill="var(--royal)"/>
      <rect x="0" y="238" width="760" height="16" fill="var(--red)"/>
      <polygon points="40,250 720,250 700,340 70,360" fill="var(--red)"/>
    </svg>
    <h1 class="headline">Lighting Issue Detected<br>On Your Property</h1>
    <p class="subhead">During our routine night inspection,<br>we noted the following item(s):</p>

    <ul class="checklist">
      <li><span class="checkbox"></span>Building Lights Out</li>
      <li><span class="checkbox"></span>Pole Lights Out</li>
      <li><span class="checkbox"></span>Sign Not Illuminated</li>
      <li><span class="checkbox"></span>Other<span class="write-line"></span></li>
    </ul>

    <div class="notes-box"><span class="notes-label">NOTES</span></div>
    <div class="action-tab">We can provide a quote or dispatch<br>service right away.</div>

    <div class="photo photo-fixtures" role="img" aria-label="Photo of a technician servicing parking lot pole light fixtures"></div>
    <div class="photo photo-truck" role="img" aria-label="Photo of a white bucket service truck with traffic cones"></div>

    <div class="brand"><span class="brand-dot"></span>Brovane Fixture Inc.</div>

    <footer class="contact-bar">
      <div class="phone-block">
        <svg width="30" height="30" viewBox="0 0 24 24" aria-hidden="true"><path fill="#fff" d="M6.6 10.8a15.1 15.1 0 0 0 6.6 6.6l2.2-2.2c.3-.3.7-.4 1-.2 1.1.4 2.3.6 3.6.6.6 0 1 .4 1 1V20c0 .6-.4 1-1 1A17 17 0 0 1 3 4c0-.6.4-1 1-1h3.5c.6 0 1 .4 1 1 0 1.3.2 2.5.6 3.6.1.3 0 .7-.2 1z"/></svg>
        877-514-0862
      </div>
      <div class="web-block">
        <span>
          <svg width="16" height="12" viewBox="0 0 16 12" aria-hidden="true"><rect x="0.5" y="0.5" width="15" height="11" fill="none" stroke="#fff"/><path d="M0.5 0.5 8 7 15.5 0.5" fill="none" stroke="#fff"/></svg>
          Service@BrovaneFixture.com
        </span>
        <span>
          <svg width="16" height="16" viewBox="0 0 16 16" aria-hidden="true"><circle cx="8" cy="8" r="7" fill="none" stroke="#fff"/><ellipse cx="8" cy="8" rx="3" ry="7" fill="none" stroke="#fff"/><path d="M1 8h14" stroke="#fff"/></svg>
          www.BrovaneFixture.com
        </span>
      </div>
    </footer>
  </article>
</body>
</html>
```